Business Card Design Project

We are rebranding an existing automotive collision repair business. The business is called dentworks garage. I have attached logo but I'm not tied to that. I want to leave this wide open.

I want this card to say we are professional, competent, cutting edge. We are focused on customers and use a lot of the latest technology to make the customer experience different. We sign customers in on iPads. Paperwork I signed electronically and updates are sent via text, email, logging on a website or as they wish. I want this innovation and image to come through in our cards

Target Market(s)

60%. Women 40% men. Age 35-60

Industry/Entity Type

Automotive

Requirements
Must have
• The card must have name, title, phone,email, cell, web page

```html
<!DOCTYPE html>
<html lang="en">
<head>
<meta charset="utf-8">
<title>Dentworks Garage – Business Card</title>
<link href="https://fonts.googleapis.com/css2?family=Source+Sans+3:wght@400;600;700&display=swap" rel="stylesheet">
<style>
  :root {
    --page-bg: #e8e8e8;
    --card-bg: #000000;
    --brand-green: #8cc43f;
    --text-white: #ffffff;
    --text-soft: #e6e6e6;
  }
  * { margin: 0; padding: 0; box-sizing: border-box; }
  html, body {
    width: 1200px;
    height: 931px;
    overflow: hidden;
    background: var(--page-bg);
    font-family: "Source Sans 3", "Myriad Pro", Arial, sans-serif;
  }
  .canvas {
    position: relative;
    width: 1200px;
    height: 931px;
  }
  .card {
    position: absolute;
    left: 256px;
    width: 702px;
    height: 384px;
    background: var(--card-bg);
    border-radius: 34px;
    overflow: hidden;
  }
  .card--front { top: 60px; }
  .card--back { top: 491px; }

  .brand {
    position: absolute;
    text-align: center;
    color: var(--brand-green);
    font-weight: 700;
    line-height: 1;
    white-space: nowrap;
  }
  .card--front .brand {
    left: 40px;
    top: 192px;
    width: 300px;
    font-size: 36px;
  }

  .contact {
    position: absolute;
    left: 418px;
    top: 87px;
    color: var(--text-white);
  }
  .contact__name {
    font-size: 23px;
    font-weight: 700;
    line-height: 1.1;
  }
  .contact__title {
    font-size: 22px;
    font-weight: 400;
    line-height: 1.1;
  }
  .contact__list {
    list-style: none;
    margin-top: 27px;
    font-size: 14px;
    line-height: 17px;
    color: var(--text-soft);
  }
  .contact__item {
    display: flex;
    align-items: flex-start;
  }
  .contact__item--address { margin-bottom: 17px; }
  .contact__icon {
    width: 16px;
    height: 16px;
    margin-right: 8px;
    flex-shrink: 0;
    fill: var(--brand-green);
  }

  .card--back .brand {
    left: 0;
    width: 100%;
    top: 138px;
    font-size: 64px;
  }
  .web-line {
    position: absolute;
    left: 0;
    width: 100%;
    top: 298px;
    text-align: center;
    font-size: 23px;
    color: var(--brand-green);
    font-weight: 400;
  }
  .web-line strong { font-weight: 700; }
</style>
</head>
<body>
<main class="canvas">

  <section class="card card--front" aria-label="Card front">
    <div class="brand">Dentworks Garage</div>

    <div class="contact">
      <p class="contact__name">Derek Halloway</p>
      <p class="contact__title">Owner</p>
      <ul class="contact__list">
        <li class="contact__item contact__item--address">
          <svg class="contact__icon" viewBox="0 0 16 16" aria-hidden="true"><path d="M8 0C4.9 0 2.5 2.4 2.5 5.4 2.5 9.5 8 16 8 16s5.5-6.5 5.5-10.6C13.5 2.4 11.1 0 8 0zm0 7.6a2.3 2.3 0 1 1 0-4.6 2.3 2.3 0 0 1 0 4.6z"/></svg>
          <span>418 Route 9 east Linden,<br>NJ 07036</span>
        </li>
        <li class="contact__item">
          <svg class="contact__icon" viewBox="0 0 16 16" aria-hidden="true"><path d="M4.5 1h7c.6 0 1 .4 1 1v12c0 .6-.4 1-1 1h-7c-.6 0-1-.4-1-1V2c0-.6.4-1 1-1zm.8 2v9h5.4V3H5.3zM8 12.6a.8.8 0 1 0 0 1.6.8.8 0 0 0 0-1.6z"/></svg>
          <span>908-555-0142</span>
        </li>
        <li class="contact__item">
          <svg class="contact__icon" viewBox="0 0 16 16" aria-hidden="true"><path d="M1 4h3v10H1zM5 3h10v11H5zm1.5 1.5v3h7v-3zm0 4.5v1.5h2V9zm3 0v1.5h2V9zm3 0v1.5h1V9zm-6 2.5V13h2v-1.5zm3 0V13h2v-1.5z"/></svg>
          <span>908-555-0187</span>
        </li>
        <li class="contact__item">
          <svg class="contact__icon" viewBox="0 0 16 16" aria-hidden="true"><path d="M1 6l7-4.5L15 6v8H1zm1.6 1.2V12.6h10.8V7.2L8 10.6z"/></svg>
          <span>derek@dentworksgarage.com</span>
        </li>
        <li class="contact__item">
          <svg class="contact__icon" viewBox="0 0 16 16" aria-hidden="true"><path d="M8 1a7 7 0 1 0 0 14A7 7 0 0 0 8 1zm0 1.5c.9 0 1.9 1.7 2.2 4.3H5.8C6.1 4.2 7.1 2.5 8 2.5zM2.6 8.2h1.9c0 1.6.3 3 .8 4A5.5 5.5 0 0 1 2.6 8.2zm1.9-1.4H2.6a5.5 5.5 0 0 1 2.7-3.9c-.5 1-.8 2.3-.8 3.9zm3.5 6.7c-.9 0-1.9-1.7-2.2-4.3h4.4c-.3 2.6-1.3 4.3-2.2 4.3zm2.7-1.3c.5-1 .8-2.4.8-4h1.9a5.5 5.5 0 0 1-2.7 4zm.8-5.4c0-1.6-.3-2.9-.8-3.9a5.5 5.5 0 0 1 2.7 3.9z"/></svg>
          <span>www.dentworksgarage.com</span>
        </li>
      </ul>
    </div>
  </section>

  <section class="card card--back" aria-label="Card back">
    <div class="brand">Dentworks Garage</div>
    <p class="web-line">www.<strong>dentworksgarage</strong>.com</p>
  </section>

</main>
</body>
</html>
```